The amber lantern with an elephant incorporated in the background

Target Market(s)

Real estate

Industry/Entity Type

Real Estate

Contact Information for Business Card

On back on want my name & number
In front I want the business name, "the amber lantern", below to say staging & design

Logo Text

The amber lantern

Font styles to use
Serif

Colors
000000

Requirements
Must have
• I want an elephant behind the writing in gold transperant

```html
<!DOCTYPE html>
<html lang="en">
<head>
<meta charset="utf-8">
<title>The Amber Lantern — Business Cards</title>
<link href="https://fonts.googleapis.com/css2?family=Encode+Sans+Condensed:wght@500;600&family=PT+Serif&display=swap" rel="stylesheet">
<style>
  :root {
    --page: #e9e6e1;
    --ink: #050505;
    --gold: #e2a027;
    --text-gold: #e8a21e;
  }
  html, body {
    margin: 0;
    width: 1200px;
    height: 1200px;
    overflow: hidden;
    background: var(--page);
  }
  .sheet {
    position: relative;
    width: 1200px;
    height: 1200px;
  }
  .card {
    position: absolute;
    left: 120px;
    width: 960px;
    height: 548px;
    background: var(--ink);
    overflow: hidden;
    box-shadow: 0 6px 18px rgba(0,0,0,0.18);
  }
  .card--back { top: 36px; }
  .card--front { top: 616px; }
  .card svg.art {
    position: absolute;
    inset: 0;
    width: 100%;
    height: 100%;
  }
  .brand {
    position: absolute;
    right: 70px;
    top: 40px;
    text-align: right;
    color: var(--text-gold);
  }
  .brand__the {
    font-family: "Encode Sans Condensed", sans-serif;
    font-weight: 600;
    font-size: 44px;
    line-height: 1;
    letter-spacing: 1px;
  }
  .brand__row {
    display: flex;
    align-items: baseline;
    justify-content: flex-end;
    gap: 16px;
    margin-top: 8px;
    padding-bottom: 10px;
    border-bottom: 2px solid var(--text-gold);
  }
  .brand__tagline {
    font-family: "PT Serif", serif;
    font-size: 19px;
    letter-spacing: 1px;
    text-transform: uppercase;
  }
  .brand__name {
    font-family: "Encode Sans Condensed", sans-serif;
    font-weight: 600;
    font-size: 52px;
    line-height: 1;
    text-transform: uppercase;
  }
  .brand__phone {
    font-family: "PT Serif", serif;
    font-size: 30px;
    margin-top: 14px;
    text-align: right;
  }
  .card--front .brand { top: 110px; right: 80px; }
  .person {
    position: absolute;
    left: 50px;
    bottom: 50px;
    font-family: "Encode Sans Condensed", sans-serif;
    font-weight: 600;
    font-size: 40px;
    letter-spacing: 1px;
    color: var(--ink);
    text-transform: uppercase;
  }
</style>
</head>
<body>
<div class="sheet">

  <section class="card card--back">
    <svg class="art" viewBox="0 0 960 548" xmlns="http://www.w3.org/2000/svg">
      <defs>
        <radialGradient id="statue-gold" cx="50%" cy="55%" r="65%">
          <stop offset="0%" stop-color="#f5cf4f"/>
          <stop offset="65%" stop-color="#d49c18"/>
          <stop offset="100%" stop-color="#8f6207"/>
        </radialGradient>
      </defs>
      <path class="name-panel" d="M0 185 L290 185 C300 260 275 330 300 400 C315 460 300 510 310 548 L0 548 Z" fill="var(--gold)"/>
      <rect role="img" aria-label="Photo of a golden ornamental elephant statue with raised trunk"
            x="330" y="170" width="300" height="400" rx="40" fill="url(#statue-gold)"/>
    </svg>
    <div class="brand">
      <div class="brand__the">THE</div>
      <div class="brand__row">
        <span class="brand__tagline">Staging &amp; Design</span>
        <span class="brand__name">Amber Lantern</span>
      </div>
      <div class="brand__phone">T: 123-456-7890</div>
    </div>
    <div class="person">John Doe</div>
  </section>

  <section class="card card--front">
    <svg class="art" viewBox="0 0 960 548" xmlns="http://www.w3.org/2000/svg">
      <defs>
        <radialGradient id="statue-gold-dim" cx="50%" cy="55%" r="65%">
          <stop offset="0%" stop-color="#c2941f"/>
          <stop offset="70%" stop-color="#7d5a0c"/>
          <stop offset="100%" stop-color="#2e2105"/>
        </radialGradient>
      </defs>
      <rect role="img" aria-label="Translucent photo of a golden elephant statue in the background"
            x="50" y="110" width="340" height="470" rx="40" fill="url(#statue-gold-dim)" opacity="0.85"/>
    </svg>
    <div class="brand">
      <div class="brand__the">THE</div>
      <div class="brand__row">
        <span class="brand__tagline">Staging &amp; Design</span>
        <span class="brand__name">Amber Lantern</span>
      </div>
    </div>
  </section>

</div>
</body>
</html>
```